Casa and Valor Website Re-design

Already Wordpress base. Needs to be updated and better presentation. Current site: www.valorcasa.example redirected from www.casaandvalors.example
Site purpose is to offer information and get leads from potential heroes looking to buy, rent or sell a home
Here is a link to the video to be used as well: https://www.videohost.example/watch?v=Lm8RtPz3VwK

I own the video and logo
The video spells out the program. We will need a page for REALTORS to sign up, a page for our Vendors and their benefits
Steadfast Lending, Marpen Odari offers a reduced rate plus they will pay the upfront cost of the $600 VA appraisal
Hero Buyers get 25% rebate after escrow
Hero Sellers get 25% off a normal 6% Listing
A partner inspector will give a 10% off discount for heroes
Also need a page for the Hero Giving Program

Direct competitor: www.nestsforvalor.example

Target Market(s)

veterans, teachers, government employees, nurses, 1st responders

Industry/Entity Type

Realtor

Coding

Coded - Design and coding required

Number of Pages Required

5+ page

Colors
ec1f27
ffffff
3176b5

Requirements
Must have
• clean and correct throughout, ability to collect leads with FB login, or names and phone and email information. Colors are Navy Blue, Burgandy Red, and White
Nice to have
• photos

```html
<!DOCTYPE html>
<html lang="en">
<head>
<meta charset="utf-8">
<title>Casa and Valor</title>
<link href="https://fonts.googleapis.com/css2?family=Roboto:wght@300;400;500;700;900&family=Roboto+Condensed:wght@700&display=swap" rel="stylesheet">
<style>
:root{
  --navy:#1c2f63;
  --navy-deep:#14224a;
  --blue:#3176b5;
  --red:#ec1f27;
  --charcoal:#2b2d31;
  --ink:#222;
  --muted:#666;
  --light:#f2f2f2;
  --white:#fff;
}
*{box-sizing:border-box;margin:0;padding:0}
html,body{width:1200px;height:2528px;overflow:hidden}
body{font-family:"Roboto",Arial,sans-serif;color:var(--ink);background:var(--white)}
.topbar{height:48px;background:var(--navy-deep);color:#cfd6e8;font-size:13px;display:flex;justify-content:space-between;align-items:center;padding:0 72px}
.topbar span{display:inline-flex;align-items:center;gap:8px;margin-left:24px}
.header{height:92px;display:flex;align-items:center;justify-content:space-between;padding:0 72px;border-bottom:3px solid var(--red)}
.brand{display:flex;align-items:center;gap:10px;font-weight:700;font-size:26px;color:var(--navy)}
.brand i{width:18px;height:18px;border-radius:50%;background:var(--red);display:block}
.nav{display:flex;gap:30px;font-size:13px;font-weight:500;color:var(--navy);text-transform:uppercase}
.nav a:first-child{color:var(--red)}
.hero{height:420px;position:relative;background:linear-gradient(180deg,#8fb4dc 0%,#c9d7e4 40%,#b8a98f 70%,#4e6b37 100%)}
.hero-card{position:absolute;left:50%;top:180px;transform:translateX(-50%);background:rgba(20,34,74,.82);color:var(--white);text-align:center;padding:26px 60px}
.hero-card h1{font-family:"Roboto Condensed",sans-serif;font-size:44px;letter-spacing:1px}
.hero-card p{font-size:14px;font-weight:700;color:#ffb3b5;letter-spacing:1px;margin-top:4px}
.paths{display:flex;height:220px}
.path{flex:1;color:var(--white);padding:30px 40px}
.path h3{font-size:18px;font-weight:700;margin-bottom:12px;text-transform:uppercase}
.path p{font-size:13px;line-height:1.55;opacity:.9;max-width:300px}
.path .btn{display:inline-block;margin-top:16px;border:1px solid rgba(255,255,255,.7);font-size:11px;padding:7px 16px;text-transform:uppercase}
.path.buy{background:var(--navy)}
.path.rent{background:var(--charcoal);text-align:center}
.path.rent p{margin:0 auto}
.path.sell{background:var(--red);text-align:right}
.path.sell p{margin-left:auto}
.welcome{height:540px;text-align:center;padding:60px 120px 0}
.welcome h2{font-size:36px;color:var(--navy);font-weight:700}
.welcome .lead{font-size:14px;line-height:1.7;color:var(--muted);margin:22px auto 0;max-width:920px}
.heroes{display:flex;justify-content:space-between;margin-top:46px}
.hero-type{width:280px}
.hero-type .mark{width:64px;height:64px;border-radius:50%;background:var(--navy);margin:0 auto 12px}
.hero-type h4{font-size:20px;color:var(--ink);margin-bottom:10px}
.hero-type p{font-size:13px;line-height:1.6;color:var(--muted)}
.rewards{height:280px;background:linear-gradient(90deg,#1a3a86,#2a58a8 50%,#1a3a86);color:var(--white);text-align:center;padding-top:44px}
.rewards h2{font-size:38px;font-weight:900;text-transform:uppercase}
.rewards .qual{font-size:13px;margin-top:14px;opacity:.85}
.rewards .cta{font-size:15px;margin-top:8px;font-weight:500}
.lead-form{display:flex;justify-content:center;align-items:center;gap:16px;margin-top:30px;font-size:14px}
.lead-form .field{width:240px;height:38px;background:var(--white);display:flex;align-items:center;justify-content:flex-end;padding-right:12px;color:var(--muted)}
.lead-form .submit{height:38px;background:var(--red);padding:0 26px;display:flex;align-items:center;gap:8px;font-weight:700;text-transform:uppercase}
.advantages{height:320px;display:flex;padding:46px 72px 0;gap:40px}
.adv-text{width:480px}
.adv-text h2{font-size:30px;color:var(--navy);font-weight:900;text-transform:uppercase;border-bottom:3px solid var(--red);display:inline-block;padding-bottom:4px;margin-bottom:20px}
.adv-item{display:flex;gap:12px;margin-bottom:14px}
.adv-item .tick{flex:none;margin-top:2px}
.adv-item h5{font-size:14px;color:var(--red);font-weight:700}
.adv-item p{font-size:12px;color:var(--muted);line-height:1.5}
.video{flex:1;height:250px;position:relative;background:linear-gradient(135deg,#6d7a4f,#3b4630 60%,#25301f)}
.video .play{position:absolute;left:50%;top:50%;transform:translate(-50%,-50%)}
.testimonials{height:380px;background:var(--light);text-align:center;padding-top:40px}
.testimonials h2{font-size:34px;font-weight:900;text-transform:uppercase;color:var(--ink)}
.testimonials .rule{width:60px;height:3px;background:var(--red);margin:10px auto 20px}
.avatar{width:70px;height:70px;border-radius:50%;background:#b58e6e;margin:0 auto 10px}
.testimonials .name{font-size:13px;font-weight:700}
.testimonials blockquote{font-size:14px;font-style:italic;color:var(--muted);line-height:1.7;max-width:820px;margin:16px auto 0}
.footer{height:200px;background:#3a3b3f;display:flex;justify-content:space-around;align-items:center;padding:0 80px;color:#ddd;font-size:15px}
.footer .item{display:flex;align-items:center;gap:14px}
.footer .icon{width:46px;height:46px;border-radius:50%;background:#55575c;display:flex;align-items:center;justify-content:center}
.copyright{height:28px;background:#1d1e21;color:#999;font-size:11px;text-align:center;line-height:28px}
</style>
</head>
<body>
<div class="topbar">
  <div>Serving heroes across the region</div>
  <div>
    <span><svg width="12" height="12" viewBox="0 0 24 24" fill="#cfd6e8"><path d="M6.6 10.8a15 15 0 0 0 6.6 6.6l2.2-2.2a1 1 0 0 1 1-.25 11.4 11.4 0 0 0 3.6.57 1 1 0 0 1 1 1V20a1 1 0 0 1-1 1A17 17 0 0 1 3 4a1 1 0 0 1 1-1h3.5a1 1 0 0 1 1 1c0 1.25.2 2.45.57 3.57a1 1 0 0 1-.25 1z"/></svg>(555) 014-2398</span>
    <span><svg width="13" height="10" viewBox="0 0 26 20"><rect x="1" y="1" width="24" height="18" fill="none" stroke="#cfd6e8" stroke-width="2"/><path d="M1 1l12 10L25 1" fill="none" stroke="#cfd6e8" stroke-width="2"/></svg>hello@valorcasa.example</span>
  </div>
</div>
<header class="header">
  <div class="brand"><i></i>Casa &amp; Valor</div>
  <nav class="nav"><a>Home</a><a>How It Works</a><a>Hero Advantages</a><a>Realtors</a><a>Hero Giving Program</a><a>Contact</a></nav>
</header>
<section class="hero" role="img" aria-label="Photograph of a large two-storey family home with a tiled roof and green lawn under a blue sky">
  <div class="hero-card">
    <h1>CASA &amp; VALOR</h1>
    <p>GET CASH BACK WITH PURCHASE OF HOME</p>
  </div>
</section>
<section class="paths">
  <div class="path buy"><h3>Buy</h3><p>Find a home you love and earn a cash rebate after escrow closes. Our agents guide heroes through every step of the purchase.</p><span class="btn">Learn more</span></div>
  <div class="path rent"><h3>Rent</h3><p>Search rental homes near your work with agents who understand shift schedules, deployments and the needs of busy service families.</p><span class="btn">Learn more</span></div>
  <div class="path sell"><h3>Sell a Home</h3><p>List your home with a trusted local agent and keep more of your equity with a reduced listing fee for heroes.</p><span class="btn">Learn more</span></div>
</section>
<section class="welcome">
  <h2>Welcome to Casa &amp; Valor</h2>
  <p class="lead">Casa and Valor thanks the people who serve our communities. Veterans, teachers, nurses, government employees and first responders can save thousands when they buy, sell or rent a home through our network. Local agents, lenders and inspectors share part of their fees as a reward for your service, so more of your money stays with your family.</p>
  <div class="heroes">
    <div class="hero-type"><div class="mark" role="img" aria-label="Police officer icon"></div><h4>Police Officers</h4><p>Officers who protect our streets earn cash back on every home they buy or sell with our agents.</p></div>
    <div class="hero-type"><div class="mark" role="img" aria-label="Medical personnel icon"></div><h4>Medical Personnel</h4><p>Nurses, doctors and medics receive rebates and partner discounts when they move to a new home.</p></div>
    <div class="hero-type"><div class="mark" role="img" aria-label="Firefighter icon"></div><h4>Firefighters</h4><p>Firefighters and rescue crews keep more of their equity with reduced fees and local partner savings.</p></div>
  </div>
</section>
<section class="rewards" role="img" aria-label="Blue-tinted background photo of service members">
  <h2>Get Your Hero Rewards!</h2>
  <p class="qual">Qualifying Heroes: Firefighters, Law Enforcement, Military, Nurses, Medical &amp; Healthcare Professionals, EMS, Teachers</p>
  <p class="cta">Connect with a local specialist today to maximize your savings</p>
  <div class="lead-form">
    <span>I am a</span><div class="field">&#9662;</div>
    <span>I am interested in</span><div class="field">&#9662;</div>
    <div class="submit">Continue <svg width="14" height="14" viewBox="0 0 24 24"><circle cx="12" cy="12" r="11" fill="#fff"/><path d="M10 7l5 5-5 5" fill="none" stroke="#ec1f27" stroke-width="3"/></svg></div>
  </div>
</section>
<section class="advantages">
  <div class="adv-text">
    <h2>Hero Advantages</h2>
    <div class="adv-item"><svg class="tick" width="18" height="18" viewBox="0 0 24 24"><circle cx="12" cy="12" r="11" fill="#ec1f27"/><path d="M7 12l3 3 7-7" fill="none" stroke="#fff" stroke-width="2.5"/></svg><div><h5>Hero Buyers get 25% rebate after escrow</h5><p>Your rebate is paid once escrow closes, giving you extra funds for moving costs or new furniture.</p></div></div>
    <div class="adv-item"><svg class="tick" width="18" height="18" viewBox="0 0 24 24"><circle cx="12" cy="12" r="11" fill="#ec1f27"/><path d="M7 12l3 3 7-7" fill="none" stroke="#fff" stroke-width="2.5"/></svg><div><h5>Hero Sellers get 25% off a normal 6% Listing</h5><p>Sell with an experienced local agent and keep more equity thanks to our reduced listing commission.</p></div></div>
    <div class="adv-item"><svg class="tick" width="18" height="18" viewBox="0 0 24 24"><circle cx="12" cy="12" r="11" fill="#ec1f27"/><path d="M7 12l3 3 7-7" fill="none" stroke="#fff" stroke-width="2.5"/></svg><div><h5>Home inspections get a 10% off discount for heroes</h5><p>Book a full home inspection with a trusted partner and save on the cost before you close.</p></div></div>
  </div>
  <div class="video" role="img" aria-label="Video still of a soldier walking with his family outdoors">
    <svg class="play" width="70" height="70" viewBox="0 0 70 70"><circle cx="35" cy="35" r="33" fill="rgba(255,255,255,.85)"/><path d="M28 22l20 13-20 13z" fill="#1c2f63"/></svg>
  </div>
</section>
<section class="testimonials">
  <h2>Testimonials</h2>
  <div class="rule"></div>
  <div class="avatar" role="img" aria-label="Portrait photo of the reviewer"></div>
  <p class="name">Dana Rowe, Hero Buyer</p>
  <blockquote>&ldquo;As a nurse working long shifts, I never thought buying a home would be this easy. My agent handled every detail, the inspection discount helped, and the rebate after closing paid for our move. I tell every coworker about this program.&rdquo;</blockquote>
</section>
<footer class="footer">
  <div class="item"><div class="icon"><svg width="20" height="20" viewBox="0 0 24 24" fill="#ddd"><path d="M6.6 10.8a15 15 0 0 0 6.6 6.6l2.2-2.2a1 1 0 0 1 1-.25 11.4 11.4 0 0 0 3.6.57 1 1 0 0 1 1 1V20a1 1 0 0 1-1 1A17 17 0 0 1 3 4a1 1 0 0 1 1-1h3.5a1 1 0 0 1 1 1c0 1.250.2 2.45.57 3.57a1 1 0 0 1-.25 1z"/></svg></div>(555) 014-2398</div>
  <div class="item"><div class="icon"><svg width="20" height="16" viewBox="0 0 26 20"><rect x="1" y="1" width="24" height="18" fill="none" stroke="#ddd" stroke-width="2"/><path d="M1 1l12 10L25 1" fill="none" stroke="#ddd" stroke-width="2"/></svg></div>hello@valorcasa.example</div>
  <div class="item"><div class="icon"><svg width="16" height="22" viewBox="0 0 16 22"><path d="M8 0a8 8 0 0 1 8 8c0 6-8 14-8 14S0 14 0 8a8 8 0 0 1 8-8z" fill="#ddd"/><circle cx="8" cy="8" r="3" fill="#55575c"/></svg></div><div>Casa &amp; Valor, 1400 Harbor Way<br>Fairview, ST 00000</div></div>
</footer>
<div class="copyright">Copyright &copy; 2017 valorcasa.example. All Rights Reserved.</div>
</body>
</html>
```